Interior Stylist business card design needed

I need a business card for my new company in Sydney called "Pip Dunstane Designs". The business offers an interior styling and colour consultancy. My clients are generally not very design savvy (hence why they use me) and can range from being quite conservative to really wanting something "out there". They can be looking for a budget makeover or something more expensive / substantial. I'd like my business card design to be stylish (but not overly formal). I certainly don't want it to be conservative. I'd like it to stand out a bit! I don't really have any aversion to particular colours and I don't have a logo as such - my business name is really all I have.

Target Market(s)

As above - home owners, ranging from conservative to modern

Industry/Entity Type

Conservative

Contact Information for Business Card

Pip Dunstane Designs
Colour consultancy and interior styling
ph: 0417 382 605
email: pipdunstane@harvolink.net.au

Requirements
Should not have
• Old fashioned writing or motifs. No Times Roman font!!

```html
<!DOCTYPE html>
<html lang="en">
<head>
<meta charset="utf-8">
<title>Pip Dunstane Designs – Business Card</title>
<link href="https://fonts.googleapis.com/css2?family=Lato:wght@400;700;900&display=swap" rel="stylesheet">
<style>
  :root {
    --canvas-bg: #ece7df;
    --card-black: #000000;
    --text-white: #ffffff;
    --band-red: #ed1c24;
    --band-teal: #13b5a8;
    --band-purple: #7b4a86;
  }
  * { margin: 0; padding: 0; box-sizing: border-box; }
  html, body {
    width: 1200px;
    height: 1000px;
    overflow: hidden;
    background: var(--canvas-bg);
    font-family: "Lato", Arial, sans-serif;
  }
  .canvas {
    position: relative;
    width: 1200px;
    height: 1000px;
  }
  .card {
    position: absolute;
    top: 349px;
    width: 536px;
    height: 302px;
    background: var(--card-black);
    color: var(--text-white);
    box-shadow: 3px 4px 8px rgba(0,0,0,0.35);
    overflow: hidden;
  }
  .card--front { left: 46px; }
  .card--back { left: 618px; }

  .brand { position: absolute; }
  .brand__name {
    font-weight: 700;
    font-size: 24px;
    line-height: 1;
    letter-spacing: 0.1px;
  }
  .brand__tagline {
    font-weight: 700;
    font-size: 12.5px;
    line-height: 1;
    margin-top: 4px;
  }
  .card--front .brand {
    top: 25px;
    right: 27px;
    text-align: left;
  }
  .card--back .brand {
    top: 131px;
    left: 149px;
  }

  .contact {
    position: absolute;
    left: 26px;
    top: 213px;
    list-style: none;
  }
  .contact__item {
    display: flex;
    align-items: center;
    gap: 7px;
    font-weight: 700;
    font-size: 17px;
    height: 24px;
    margin-bottom: 9px;
  }
  .contact__icon { width: 19px; height: 19px; flex: none; }

  .colour-bands {
    position: absolute;
    left: 0;
    bottom: 0;
    width: 100%;
    height: 13px;
    display: flex;
  }
  .colour-bands span { flex: 1; }
  .band--red { background: var(--band-red); }
  .band--teal { background: var(--band-teal); }
  .band--purple { background: var(--band-purple); }
</style>
</head>
<body>
<div class="canvas">

  <section class="card card--front" aria-label="Card front">
    <div class="brand">
      <div class="brand__name">Pip Dunstane Designs</div>
      <div class="brand__tagline">colour consultancy and interior styling</div>
    </div>

    <ul class="contact">
      <li class="contact__item">
        <svg class="contact__icon" viewBox="0 0 20 20" aria-hidden="true">
          <circle cx="10" cy="10" r="9.5" fill="#fff"/>
          <path d="M6.2 4.6c.5-.3 1.1-.2 1.4.3l1 1.7c.3.5.2 1-.2 1.4l-.7.6c.5 1.3 1.5 2.4 2.8 3.1l.6-.7c.4-.4.9-.5 1.4-.2l1.7 1c.5.3.6.9.3 1.4l-.6.9c-.5.7-1.4 1-2.2.7-2.9-1-5.2-3.3-6.2-6.2-.3-.8 0-1.7.7-2.2z" fill="#000"/>
        </svg>
        <span>0417 382 605</span>
      </li>
      <li class="contact__item">
        <svg class="contact__icon" viewBox="0 0 20 20" aria-hidden="true">
          <circle cx="10" cy="10" r="9.5" fill="#fff"/>
          <rect x="5" y="6.5" width="10" height="7" rx="0.8" fill="#000"/>
          <path d="M5.4 7l4.6 3.6L14.6 7" fill="none" stroke="#fff" stroke-width="1"/>
        </svg>
        <span>pipdunstane@harvolink.net.au</span>
      </li>
    </ul>

    <div class="colour-bands" aria-hidden="true">
      <span class="band--red"></span>
      <span class="band--teal"></span>
      <span class="band--purple"></span>
    </div>
  </section>

  <section class="card card--back" aria-label="Card back">
    <div class="brand">
      <div class="brand__name">Pip Dunstane Designs</div>
      <div class="brand__tagline">colour consultancy and interior styling</div>
    </div>

    <div class="colour-bands" aria-hidden="true">
      <span class="band--purple"></span>
      <span class="band--teal"></span>
      <span class="band--red"></span>
    </div>
  </section>

</div>
</body>
</html>
```